Steelcrest Process Systems. Needs a Business Card Design

We need a business card design for an engineering company which supplies industrial components (pumps, compressors, mechanical seals) provides repairs and services for above mentioned equipments. We offer a uniqe engineering solutions which help our customers to increase the productivness of their manufacturings, and energy savings.

Target Market(s)

Chemical and energy plants, refineries. Food industry and private consumers in a less.

Industry/Entity Type

Business

Contact Information for Business Card

Stylish and sleek design oriented on industrial area.

Requirements
Should not have
• company name shortening

```html
<!DOCTYPE html>
<html lang="en">
<head>
<meta charset="utf-8">
<title>Steelcrest Process Systems – Business Card</title>
<link rel="stylesheet" href="https://fonts.googleapis.com/css2?family=Open+Sans:wght@400;600;700&display=swap">
<style>
  :root {
    --page: #e9e9ec;
    --brand-blue: #1f3f94;
    --deep-blue: #163483;
    --bright-blue: #2a55b5;
    --accent-red: #e23b55;
    --accent-orange: #f0a232;
    --rule-blue: #5b6fae;
    --text-grey: #555a63;
    --card-white: #ffffff;
  }
  * { box-sizing: border-box; margin: 0; padding: 0; }
  html, body {
    width: 1200px; height: 843px; overflow: hidden;
    background: var(--page);
    font-family: "Open Sans", Arial, sans-serif;
  }
  .sheet {
    width: 1200px; height: 843px;
    display: flex; flex-direction: column; align-items: center; justify-content: center;
    gap: 24px;
  }
  .card {
    position: relative;
    width: 680px; height: 389px;
    overflow: hidden;
    box-shadow: 0 6px 18px rgba(0,0,0,0.18);
  }

  /* Front */
  .card-front { background: linear-gradient(180deg, #ffffff 0%, #f6f7f9 100%); }
  .person { position: absolute; left: 48px; top: 98px; }
  .person-name {
    font-size: 21px; font-weight: 600; letter-spacing: 0.5px;
    color: var(--brand-blue); text-transform: uppercase; line-height: 1.1;
  }
  .person-role { font-size: 15px; color: var(--accent-red); margin-top: 2px; }
  .divider {
    position: absolute; left: 48px; top: 158px; width: 584px; height: 1.5px;
    background: var(--rule-blue);
  }
  .company {
    position: absolute; right: 48px; top: 108px;
    display: flex; align-items: center; gap: 10px;
  }
  .company-dot { width: 14px; height: 14px; border-radius: 50%; background: var(--brand-blue); }
  .company-name { font-size: 22px; font-weight: 700; color: var(--brand-blue); letter-spacing: -0.2px; }
  .contacts { position: absolute; left: 48px; top: 176px; list-style: none; }
  .contacts li {
    display: flex; align-items: center; gap: 9px;
    font-size: 14px; color: var(--text-grey); line-height: 23px;
  }
  .contacts svg { width: 13px; height: 13px; fill: var(--brand-blue); flex: none; }
  .address {
    position: absolute; right: 48px; top: 268px; text-align: right;
    font-size: 14px; color: var(--text-grey); line-height: 22px;
  }
  .footer-band { position: absolute; left: 0; bottom: 0; width: 680px; height: 22px; }

  /* Back */
  .card-back {
    background: linear-gradient(160deg, var(--bright-blue) 0%, var(--deep-blue) 100%);
    display: flex; flex-direction: column; align-items: center; justify-content: center;
    gap: 60px;
  }
  .back-company { display: flex; align-items: center; gap: 12px; margin-top: 50px; }
  .back-company .company-dot { background: #ffffff; width: 18px; height: 18px; }
  .back-company .company-name { color: #ffffff; font-size: 26px; }
  .back-web { font-size: 13px; color: #ffffff; letter-spacing: 3px; opacity: 0.9; }
</style>
</head>
<body>
<main class="sheet">

  <section class="card card-front" aria-label="Business card front">
    <div class="person">
      <p class="person-name">Daniel Rourke</p>
      <p class="person-role">CEO/Founder</p>
    </div>

    <div class="company">
      <span class="company-dot"></span>
      <span class="company-name">Steelcrest Process Systems</span>
    </div>

    <div class="divider"></div>

    <ul class="contacts">
      <li>
        <svg viewBox="0 0 16 16" aria-hidden="true"><path d="M3.6 1.2l2.3 2.6-1.3 1.9c.9 2 2.6 3.7 4.6 4.6l1.9-1.3 2.6 2.3-1.6 2.5C6.7 13.5 2.5 9.3 1.2 3.9z"/></svg>
        555 014 2290
      </li>
      <li>
        <svg viewBox="0 0 16 16" aria-hidden="true"><path d="M4.5 0h7A1.5 1.5 0 0 1 13 1.5v13a1.5 1.5 0 0 1-1.5 1.5h-7A1.5 1.5 0 0 1 3 14.5v-13A1.5 1.5 0 0 1 4.5 0zM5 2v10h6V2zm3 11a1 1 0 1 0 0 2 1 1 0 0 0 0-2z"/></svg>
        555 017 3841
      </li>
      <li>
        <svg viewBox="0 0 16 16" aria-hidden="true"><path d="M1 3h14v10H1zm1.5 1.2v.3L8 8.6l5.5-4.1v-.3zm0 2.2v5.1h11V6.4L8 10.5z"/></svg>
        d.rourke@steelcrestps.com
      </li>
      <li>
        <svg viewBox="0 0 16 16" aria-hidden="true"><path d="M8 1a7 7 0 1 0 0 14A7 7 0 0 0 8 1zm0 1.6c.8 0 1.8 1.5 2.1 3.9H5.9C6.2 4.1 7.2 2.6 8 2.6zM2.7 7.5h1.6c0 .7.1 1.4.2 2H2.9a5.4 5.4 0 0 1-.2-2zm9 0h1.6a5.4 5.4 0 0 1-.2 2h-1.6c.1-.6.2-1.3.2-2zM5.9 9.5h4.2C9.8 11.9 8.8 13.4 8 13.4s-1.8-1.5-2.1-3.9z"/></svg>
        www.steelcrestps.com
      </li>
    </ul>

    <address class="address">
      4120 Foundry Road<br>
      Juneau, Alaska 99801
    </address>

    <svg class="footer-band" viewBox="0 0 680 22" preserveAspectRatio="none" aria-hidden="true">
      <polygon points="0,12 680,12 680,22 0,22" fill="var(--brand-blue)"/>
      <polygon points="470,12 540,12 546,22 476,22" fill="var(--accent-orange)"/>
      <polygon points="546,12 610,12 616,22 552,22" fill="var(--accent-red)"/>
    </svg>
  </section>

  <section class="card card-back" aria-label="Business card back">
    <div class="back-company">
      <span class="company-dot"></span>
      <span class="company-name">Steelcrest Process Systems</span>
    </div>
    <p class="back-web">www.steelcrestps.com</p>
  </section>

</main>
</body>
</html>
```